TV Appliances( Summer sale flyers) making 50.000 copies

We are a company that is based in the United Arab Emirates that deal with NEW household electronics for more than 15 years.

Company details:
- TV Appliances
-chatlyne nr for large orders: 0097150 3619 772
- company line: 009716 7184259
-tvappliances-example.ae ( new website that we are making right now)
- new email address will be provided at the later stages.

Now that the summer season is approaching, we are looking to make a flyer that include air conditioners and other items that we have for sale. we are open for any design ideas that come, but the should not be over dramatic

To get an idea of what a SALE flyer is, please go on findora and type in ''electronics flyer'' go in MAGES and you see different styles of how different companies are promoting their items.

**we are looking for a double sided flyer:(Landscape view) (A3 size)
-first page would contain our lines of Air conditioners that we have for sale.we have more than 10 different brands
(( Free delivery and fitting for Sharjah, ajman,dubai))

Brands such as : VELMO, NORBECKS, TALIVRO,QD, U-PRAXIM, ROVU,MEGAFINDLAR and much more.

Example of the first page would be :
http://www.artbidplace.example/design/4829163 ( the right segment).
but the air conditioners UNIT should be displayed like:
http://www.artbidplace.example/design/4830598 (bottom left segment)

- second page would include all other items such as TV, gas cookers, fridges, freezers, chillers, vacuums, and other household appliances that we have for sale.

we are more open to the second page design wise, so please come up with something creative.

***we are making 50.000 copies so we expect this to portray our company)***

**once the final design is chosen, we would like to keep contact with the designer as we need flyers for every season in our line of work**

Target Market(s)

normal day to day people at home

Industry/Entity Type

Electronics

Font styles to use
Serif
Sans Serif

Colors
ec1f27
3176b5
eaf1f7
cfdeed

Requirements
Must have
• item pictures, item prices, and a very nice design. (original pictures and prices will be supplied once we choose a layout and design)
• item prices will be given at the end of the project
Nice to have
• good theme, modern
Should not have
• unserious pictures & design

```html
<!DOCTYPE html>
<html lang="en">
<head>
<meta charset="utf-8">
<title>TV Appliances – Household Appliances Sale Flyer</title>
<link href="https://fonts.googleapis.com/css2?family=Open+Sans:wght@400;600;700&display=swap" rel="stylesheet">
<style>
  :root{
    --brand-red:#ec1f27;
    --brand-red-dark:#c4121a;
    --brand-blue:#3176b5;
    --brand-blue-deep:#2a6aab;
    --sky-top:#57c0ec;
    --sky-mid:#cfdeed;
    --sky-pale:#eaf1f7;
    --paper:#ffffff;
    --ink:#0b0b0b;
    --steel-light:#eceff1;
    --steel-mid:#c3c9ce;
    --steel-dark:#8c949b;
    --vacuum-red:#d2232a;
    --vacuum-red-dark:#7e0c10;
    --screen-dark:#121417;
    --chiller-dark:#19191b;
    --chiller-wood:#3b2a1f;
  }
  *{box-sizing:border-box;margin:0;padding:0}
  html,body{width:1200px;height:857px;overflow:hidden;background:var(--paper)}
  body{font-family:"Open Sans",Arial,sans-serif}
  .canvas{position:relative;width:1200px;height:857px;overflow:hidden;background:var(--paper)}
  .flyer{position:absolute;left:0;top:0;width:1220px;height:871px;transform:scale(0.98361);transform-origin:0 0}
  .sky{position:absolute;left:15px;top:12px;width:1195px;height:846px;
    background:linear-gradient(180deg,var(--sky-top) 0%,#a9d6f0 14%,var(--sky-pale) 36%,#f6f9fc 52%,#ffffff 70%)}
  .red-field{position:absolute;left:0;top:0;width:1220px;height:871px}

  .section-bar{position:absolute;background:linear-gradient(90deg,var(--brand-red-dark),var(--brand-red) 40%,var(--brand-red));
    color:#fff;font-weight:600;letter-spacing:.5px;display:flex;align-items:center;justify-content:center;
    box-shadow:0 3px 4px rgba(0,0,0,.18)}
  .section-bar--blue{background:linear-gradient(90deg,#2e9be0,var(--brand-blue) 60%,var(--brand-blue-deep))}

  .tv-frame{position:absolute;background:var(--brand-blue);border-radius:14px}
  .tv-frame::after,.label-box::after{content:"";position:absolute;inset:6px;border:2px dashed #fff;border-radius:10px}
  .tv-screen{position:absolute;left:17%;top:22%;width:68%;height:55%;
    background:linear-gradient(160deg,#3a3f45 0%,var(--screen-dark) 35%,#000 100%);
    border:3px solid #050505;z-index:1;box-shadow:0 4px 6px rgba(0,0,0,.3)}
  .sale-ribbon{position:absolute;left:-4px;top:18px;width:96px;height:32px;background:var(--ink);
    transform:rotate(-20deg);color:#fff;font-weight:700;font-size:22px;letter-spacing:1px;
    display:flex;align-items:center;justify-content:center;z-index:2;box-shadow:0 2px 3px rgba(0,0,0,.3)}

  .tv-label{position:absolute;left:0;width:1220px;top:285px;text-align:center;
    font-size:74px;font-weight:400;color:var(--ink);letter-spacing:-.5px;line-height:1.2}

  .label-box{position:absolute;background:var(--brand-blue);border-radius:12px;color:#fff;
    display:flex;align-items:center;justify-content:center;text-align:center;line-height:1.45;z-index:2}
  .label-box--lg{font-size:15px}
  .label-box--sm{font-size:11px}

  .product-photo{position:absolute;z-index:1;box-shadow:0 5px 9px rgba(0,0,0,.28)}
  .product-photo--fridge{border-radius:6px;
    background:linear-gradient(90deg,var(--steel-dark) 0%,var(--steel-light) 22%,var(--steel-mid) 48%,#9aa2a9 50%,var(--steel-mid) 52%,var(--steel-light) 78%,var(--steel-dark) 100%)}
  .product-photo--vacuum{border-radius:46% 46% 32% 32%;
    background:linear-gradient(155deg,#ef4a50 0%,var(--vacuum-red) 40%,var(--vacuum-red-dark) 100%)}
  .product-photo--freezer{border-radius:6px;
    background:linear-gradient(180deg,var(--steel-light) 0%,var(--steel-light) 18%,#a9b1b8 20%,var(--steel-mid) 45%,var(--steel-dark) 100%)}
  .product-photo--chiller{border:5px solid #a7adb2;border-radius:4px;
    background:linear-gradient(180deg,#0c0c0d 0%,var(--chiller-dark) 12%,var(--chiller-wood) 50%,var(--chiller-dark) 88%,#0c0c0d 100%)}

  .delivery-note{position:absolute;left:35px;top:795px;color:#fff;font-weight:700;font-size:16px;line-height:1.4}
</style>
</head>
<body>
<div class="canvas">
<div class="flyer">
  <div class="sky"></div>

  <svg class="red-field" viewBox="0 0 1220 871" aria-hidden="true">
    <defs>
      <linearGradient id="redSweep" x1="0" y1="0" x2="1" y2="1">
        <stop offset="0" stop-color="#ec1f27"/>
        <stop offset="0.45" stop-color="#d9161e"/>
        <stop offset="0.6" stop-color="#f0444a"/>
        <stop offset="0.75" stop-color="#e01c24"/>
        <stop offset="1" stop-color="#c4121a"/>
      </linearGradient>
    </defs>
    <polygon fill="url(#redSweep)" points="840,430 1210,418 1210,858 15,858 15,780 418,780 440,642 752,628"/>
  </svg>

  <div class="section-bar" style="left:28px;top:15px;width:318px;height:37px;font-size:24px;justify-content:flex-start;padding-left:24px">FLAT SCREEN TV</div>

  <div class="tv-frame" style="left:115px;top:88px;width:210px;height:172px"><div class="sale-ribbon">SALE</div><div class="tv-screen" role="img" aria-label="Flat screen TV product photo"></div></div>
  <div class="tv-frame" style="left:375px;top:94px;width:210px;height:172px"><div class="sale-ribbon">SALE</div><div class="tv-screen" role="img" aria-label="Flat screen TV product photo"></div></div>
  <div class="tv-frame" style="left:637px;top:94px;width:210px;height:172px"><div class="sale-ribbon">SALE</div><div class="tv-screen" role="img" aria-label="Flat screen TV product photo"></div></div>
  <div class="tv-frame" style="left:895px;top:96px;width:210px;height:172px"><div class="sale-ribbon">SALE</div><div class="tv-screen" role="img" aria-label="Flat screen TV product photo"></div></div>

  <div class="tv-label">LABEL OF TV HERE</div>

  <div class="section-bar" style="left:18px;top:392px;width:332px;height:38px;font-size:25px">FRIDGES</div>
  <div class="section-bar" style="left:386px;top:386px;width:332px;height:39px;font-size:25px">VACUUM</div>
  <div class="section-bar" style="left:776px;top:377px;width:332px;height:38px;font-size:25px">FREEZERS</div>
  <div class="section-bar section-bar--blue" style="left:440px;top:656px;width:282px;height:35px;font-size:26px">CHILLERS</div>

  <!-- Fridges -->
  <div class="product-photo product-photo--fridge" style="left:35px;top:487px;width:70px;height:128px" role="img" aria-label="Stainless steel French-door fridge photo"></div>
  <div class="label-box label-box--lg" style="left:105px;top:495px;width:124px;height:105px">LABEL OF<br>REF HERE</div>
  <div class="product-photo product-photo--fridge" style="left:228px;top:448px;width:70px;height:130px" role="img" aria-label="Stainless steel French-door fridge photo"></div>
  <div class="label-box label-box--lg" style="left:298px;top:455px;width:127px;height:110px">LABEL OF<br>REF HERE</div>
  <div class="product-photo product-photo--fridge" style="left:228px;top:593px;width:70px;height:127px" role="img" aria-label="Stainless steel French-door fridge photo"></div>
  <div class="label-box label-box--lg" style="left:298px;top:605px;width:127px;height:105px">LABEL OF<br>REF HERE</div>
  <div class="product-photo product-photo--fridge" style="left:23px;top:656px;width:72px;height:128px" role="img" aria-label="Stainless steel French-door fridge photo"></div>
  <div class="label-box label-box--lg" style="left:95px;top:665px;width:126px;height:105px">LABEL OF<br>REF HERE</div>

  <!-- Vacuums -->
  <div class="product-photo product-photo--vacuum" style="left:516px;top:462px;width:62px;height:58px" role="img" aria-label="Red canister vacuum cleaner photo"></div>
  <div class="label-box label-box--sm" style="left:580px;top:455px;width:78px;height:63px">LABEL OF<br>REF HERE</div>
  <div class="product-photo product-photo--vacuum" style="left:474px;top:575px;width:50px;height:48px" role="img" aria-label="Red canister vacuum cleaner photo"></div>
  <div class="label-box label-box--sm" style="left:525px;top:560px;width:80px;height:65px">LABEL OF<br>REF HERE</div>
  <div class="product-photo product-photo--vacuum" style="left:626px;top:560px;width:58px;height:52px" role="img" aria-label="Red canister vacuum cleaner photo"></div>
  <div class="label-box label-box--sm" style="left:688px;top:530px;width:77px;height:65px">LABEL OF<br>REF HERE</div>

  <!-- Freezers -->
  <div class="product-photo product-photo--freezer" style="left:735px;top:455px;width:102px;height:78px" role="img" aria-label="Silver chest freezer with open lid photo"></div>
  <div class="label-box label-box--sm" style="left:835px;top:445px;width:90px;height:80px">LABEL OF<br>REF HERE</div>
  <div class="product-photo product-photo--freezer" style="left:988px;top:440px;width:102px;height:74px" role="img" aria-label="Silver chest freezer with open lid photo"></div>
  <div class="label-box label-box--sm" style="left:1090px;top:435px;width:90px;height:80px">LABEL OF<br>REF HERE</div>
  <div class="product-photo product-photo--freezer" style="left:747px;top:585px;width:102px;height:76px" role="img" aria-label="Silver chest freezer with open lid photo"></div>
  <div class="label-box label-box--sm" style="left:850px;top:580px;width:82px;height:78px">LABEL OF<br>REF HERE</div>
  <div class="product-photo product-photo--freezer" style="left:975px;top:555px;width:104px;height:76px" role="img" aria-label="Silver chest freezer with open lid photo"></div>
  <div class="label-box label-box--sm" style="left:1080px;top:548px;width:82px;height:78px">LABEL OF<br>REF HERE</div>

  <!-- Chillers -->
  <div class="product-photo product-photo--chiller" style="left:475px;top:715px;width:87px;height:136px" role="img" aria-label="Glass-door wine chiller photo"></div>
  <div class="label-box label-box--lg" style="left:562px;top:715px;width:128px;height:107px">LABEL OF<br>REF HERE</div>
  <div class="product-photo product-photo--chiller" style="left:735px;top:710px;width:88px;height:140px" role="img" aria-label="Glass-door wine chiller photo"></div>
  <div class="label-box label-box--lg" style="left:822px;top:712px;width:128px;height:108px">LABEL OF<br>REF HERE</div>
  <div class="product-photo product-photo--chiller" style="left:988px;top:712px;width:88px;height:138px" role="img" aria-label="Glass-door wine chiller photo"></div>
  <div class="label-box label-box--lg" style="left:1078px;top:712px;width:127px;height:108px">LABEL OF<br>REF HERE</div>

  <p class="delivery-note">(Free delivery and fitting for Sharjah,<br>Ajman, and Dubai)</p>
</div>
</div>
</body>
</html>
```